Web Design Project

Psychotherapy and Counselling Practice needs a landing page web design.

My business "Harbourlight Consulting" specialises in the treatment of Anxiety and Depression with a holistic approach, endeavouring to unlock the key that holds us to ransom in a life that is imbalanced, frustrating, and ultimately of our own making due to our own perceptions and behaviours.

There is much that impacts us which we cannot change, but we are always in control of how we think, and how we frame our experiences.....learning to challenge those thoughts and behaviours that are destructive and disempowering opens up a world of joyful possibility. Life is about making choices, learn to make wiser and healthier choices.......

Harbourlight Consulting has a client base of individual clients but will seek to expand to offer services to the Corporate world by offering an adjunct to employers for established "Wellness Programs".

Harbourlight Consulting is a highly professional, ethically bound business, with the needs of the client at the forefront of all we do.

Harbourlight Consulting wishes to avoid the usual "jargon driven" psychobabble offered on many counselling web pages. It aims to be stylishly presented, clean in look and with as few "words" as possible and a largely white background (faster loading and more powerful impact of what is stated), those words contained in the webpage should be meaningful, persuasive and have an impact simply at glance. Harbourlight does not want , or expect, those prospective clients in need of support , to be reading through volumes of industry driven cliches.

At this point Harbourlight is just looking for a high quality landing page. However in time this will likely expand to include other sections such as case studies, video content etc.

Target Market(s)

Those in need of emotional support, suffering mental health issues, and those simply wanting to become self aware supported by a mindful therapist.

Industry/Entity Type

Industry

Requirements
Must have
• The design must incorporate the Harbourlight logo and colour schemes found on the attached files.

```html
<!DOCTYPE html>
<html lang="en">
<head>
<meta charset="utf-8">
<title>Harbourlight Consulting</title>
<link href="https://fonts.googleapis.com/css2?family=Lato:wght@300;400;700&family=Montserrat:wght@300;400&family=Source+Sans+3:wght@300;400;600;700&display=swap" rel="stylesheet">
<style>
:root{
  --green:#8aa60e;
  --green-light:#a6c61c;
  --charcoal:#585858;
  --text:#5a5a5a;
  --muted:#6f6f6f;
  --white:#ffffff;
  --orange-top:#ffc93a;
  --orange-bottom:#f2a312;
}
*{margin:0;padding:0;box-sizing:border-box}
html,body{width:1200px;height:942px;overflow:hidden}
body{
  position:relative;
  background:radial-gradient(ellipse at 50% 35%,#fdfdfd 0%,#f4f4f4 55%,#e9e9e9 100%);
  font-family:"Lato",Arial,sans-serif;
  color:var(--text);
}
.abs{position:absolute}
.header-decor{left:0;top:60px;width:1000px;height:230px;background:linear-gradient(170deg,rgba(138,166,14,.10) 0%,rgba(138,166,14,.05) 35%,rgba(110,110,110,.06) 60%,rgba(110,110,110,0) 100%)}
.brand{left:232px;top:106px;font-family:"Montserrat",sans-serif;font-weight:300;font-size:28px;letter-spacing:.5px;color:var(--green)}
.contact{right:202px;top:76px;text-align:right}
.contact-label{font-size:13px;color:var(--muted)}
.contact-phone{font-family:"Source Sans 3",sans-serif;font-weight:400;font-size:31px;line-height:30px;color:var(--text);display:flex;align-items:center;justify-content:flex-end;gap:4px}
.contact-email{font-size:14px;color:var(--green);letter-spacing:.3px}

.panel{left:199px;top:298px;width:801px;height:332px;display:flex;box-shadow:0 16px 18px -14px rgba(0,0,0,.35)}
.form-side{width:400px;background:var(--green);position:relative}
.form-title{position:absolute;left:17px;top:13px;color:var(--white);font-family:"Source Sans 3",sans-serif;font-weight:600;font-size:26px;letter-spacing:-.6px}
.field{position:absolute;left:16px;width:353px;background:var(--white);border:1px solid #d7d7d7}
.field svg{position:absolute;left:10px;top:8px}
.field::before{content:"";position:absolute;left:37px;top:8px;height:19px;border-left:1px solid #d3d3d3}
.field span{position:absolute;left:47px;top:8px;font-family:"Source Sans 3",sans-serif;font-size:15px;font-weight:300;color:#6a6a6a}
.f-name{top:51px;height:35px}.f-email{top:92px;height:35px}.f-phone{top:134px;height:35px}.f-msg{top:178px;height:74px}
.submit{position:absolute;left:147px;top:272px;width:221px;height:43px;background:linear-gradient(180deg,var(--orange-top),var(--orange-bottom));border:1px solid #e39a10;color:#3d3d3d;font-family:"Source Sans 3",sans-serif;font-weight:700;font-size:28px;letter-spacing:-1px;display:flex;align-items:center;justify-content:center}
.info-side{flex:1;background:var(--charcoal);position:relative}
.vine-strip{position:absolute;left:0;top:30px;width:28px;height:302px;background:linear-gradient(180deg,rgba(138,166,14,0),rgba(138,166,14,.25) 40%,rgba(138,166,14,.1))}
.tagline{position:absolute;left:41px;top:127px;font-family:"Montserrat",sans-serif;font-weight:300;color:var(--white);line-height:1.2;letter-spacing:-.6px;white-space:nowrap}
.tagline .l1,.tagline .l2{font-size:18.5px}
.tagline .accent{font-size:21.5px;color:var(--green-light);font-weight:400}
.tagline .big{font-size:26.5px}
.tagline .sm{font-size:16px}

.feature{top:684px;width:205px}
.feature h2{font-family:"Source Sans 3",sans-serif;font-weight:400;font-size:20px;color:var(--green);display:flex;align-items:center;gap:12px;height:28px;white-space:nowrap}
.feature p{margin-top:19px;font-size:10px;font-weight:300;line-height:13.5px;color:#555}
.feature .more{margin-top:17px;font-size:12px;font-weight:300;color:#333}
.f1{left:211px}.f2{left:490px}.f3{left:753px}
.divider{top:688px;height:144px;border-left:1px dotted #b8b8b8}
.video{left:752px;top:726px;width:238px;height:108px;border:2px solid #d9d9d9;background:repeating-linear-gradient(90deg,#ececec 0 4px,#f4f4f4 4px 8px)}
.video .vname{position:absolute;left:0;right:0;top:44px;text-align:center;font-family:"Montserrat",sans-serif;font-weight:300;font-size:19px;color:var(--green)}
.video .play{position:absolute;left:99px;top:34px}

.footer-rule{left:202px;top:878px;width:796px;border-top:2px dotted #c9c9c9}
.copyright{left:204px;top:903px;font-size:11.5px;font-weight:300;color:#555}
.copyright b{font-weight:300;font-size:15px;color:var(--green)}
.social{left:902px;top:901px;display:flex;gap:5px}
.social i{width:13px;height:13px;border-radius:3px;background:#6f6f6f;display:block}
</style>
</head>
<body>

<div class="abs header-decor" role="img" aria-label="Sweeping green and grey curves across the header"></div>

<div class="abs brand">HARBOURLIGHT</div>

<div class="abs contact">
  <div class="contact-label">For Appointmet Call Us Today</div>
  <div class="contact-phone">
    <svg width="24" height="24" viewBox="0 0 24 24" aria-hidden="true"><path d="M6.6 10.8a15.2 15.2 0 0 0 6.6 6.6l2.2-2.2a1 1 0 0 1 1-.25 11.4 11.4 0 0 0 3.6.57 1 1 0 0 1 1 1V20a1 1 0 0 1-1 1A17 17 0 0 1 3 4a1 1 0 0 1 1-1h3.5a1 1 0 0 1 1 1c0 1.25.2 2.45.57 3.57a1 1 0 0 1-.25 1z" fill="#8aa60e"/></svg>
    0491 570 156
  </div>
  <div class="contact-email">care@harbourlight.net</div>
</div>

<section class="abs panel">
  <div class="form-side">
    <h1 class="form-title">GET MORE INFORMATION</h1>
    <div class="field f-name">
      <svg width="20" height="20" viewBox="0 0 20 20" aria-hidden="true"><circle cx="10" cy="5" r="4" fill="#6a6a6a"/><path d="M2 20v-5a5 5 0 0 1 5-5h6a5 5 0 0 1 5 5v5z" fill="#6a6a6a"/></svg>
      <span>Enter Your Name</span>
    </div>
    <div class="field f-email">
      <svg width="22" height="20" viewBox="0 0 22 20" aria-hidden="true"><path d="M1 8 11 1l10 7v11H1z" fill="none" stroke="#6a6a6a" stroke-width="1.6"/><path d="M1 8l10 7 10-7" fill="none" stroke="#6a6a6a" stroke-width="1.6"/></svg>
      <span>Enter Your Email</span>
    </div>
    <div class="field f-phone">
      <svg width="20" height="20" viewBox="0 0 24 24" aria-hidden="true"><path d="M6.6 10.8a15.2 15.2 0 0 0 6.6 6.6l2.2-2.2a1 1 0 0 1 1-.25 11.4 11.4 0 0 0 3.6.57 1 1 0 0 1 1 1V20a1 1 0 0 1-1 1A17 17 0 0 1 3 4a1 1 0 0 1 1-1h3.5a1 1 0 0 1 1 1c0 1.25.2 2.45.57 3.57a1 1 0 0 1-.25 1z" fill="#6a6a6a"/></svg>
      <span>Enter Your Phone</span>
    </div>
    <div class="field f-msg">
      <svg width="20" height="20" viewBox="0 0 20 20" aria-hidden="true"><rect x="2" y="3" width="13" height="15" fill="none" stroke="#6a6a6a" stroke-width="1.5"/><path d="M8 14l9-9 2 2-9 9H8z" fill="#6a6a6a"/></svg>
      <span>Your Message Here...</span>
    </div>
    <div class="submit">SUBMIT NOW!</div>
  </div>
  <div class="info-side">
    <div class="vine-strip" role="img" aria-label="Green climbing vine decoration"></div>
    <p class="tagline">
      <span class="l1">SPECIALISES IN THE TREATMENT</span><br>
      <span class="l2">OF </span><span class="accent">ANXIETY AND DEPRESSION</span><br>
      <span class="sm">WITH </span><span class="big">HOLISTIC APPROACH</span>
    </p>
  </div>
</section>

<article class="abs feature f1">
  <h2><svg width="30" height="26" viewBox="0 0 30 26" aria-hidden="true"><path d="M15 25 3 13A7 7 0 0 1 15 4a7 7 0 0 1 12 9z" fill="#6f6f6f"/><path d="M4 13h7l2-4 3 7 2-3h8" fill="none" stroke="#fff" stroke-width="1.4"/></svg>Wellness Programs</h2>
  <p>Lorem ipsum dolor sit amet, consectetuer adipiscing elit, sed diam nonummy nibh euismod tincidunt ut laoreet dolore magna aliquam erat volutpat. Ut wisi enim ad minim veniam, quis nostrud exerci tation ullamcorper suscipit lobortis...</p>
  <div class="more">Read More...</div>
</article>
<div class="abs divider" style="left:453px"></div>
<article class="abs feature f2">
  <h2><svg width="30" height="24" viewBox="0 0 30 24" aria-hidden="true"><path d="M2 3h10a3 3 0 0 1 3 3v17a3 3 0 0 0-3-3H2zM28 3H18a3 3 0 0 0-3 3v17a3 3 0 0 1 3-3h10z" fill="none" stroke="#6f6f6f" stroke-width="2"/><path d="M5 8h7M5 12h7M5 16h7M18 8h7M18 12h7M18 16h7" stroke="#6f6f6f" stroke-width="1.5"/></svg>Case Studies</h2>
  <p>Lorem ipsum dolor sit amet, consectetuer adipiscing elit, sed diam nonummy nibh euismod tincidunt ut laoreet dolore magna aliquam erat volutpat. Ut wisi enim ad minim veniam, quis nostrud exerci tation ullamcorper suscipit lobortis...</p>
  <div class="more">Read More...</div>
</article>
<div class="abs divider" style="left:722px"></div>
<article class="abs feature f3">
  <h2><svg width="26" height="24" viewBox="0 0 26 24" aria-hidden="true"><rect x="1" y="9" width="24" height="14" fill="#6f6f6f"/><path d="M1 3l23-2 .7 5-23 2z" fill="#6f6f6f"/></svg>Watch Video</h2>
</article>
<div class="abs video">
  <div class="vname">HARBOURLIGHT</div>
  <svg class="play" width="38" height="38" viewBox="0 0 38 38" aria-hidden="true"><circle cx="19" cy="19" r="17" fill="#f2f2f2" stroke="#9a9a9a" stroke-width="2.5"/><path d="M14 10l13 9-13 9z" fill="#111"/></svg>
</div>

<div class="abs footer-rule"></div>
<div class="abs copyright">© 2013 <b>Harbourlightconsulting</b>. All rights reserved</div>
<div class="abs social" aria-label="Social links"><i></i><i></i><i></i><i></i><i></i></div>

</body>
</html>
```